Calendar Ad / Flyer

Our law firm needs a calendar ad to place in a local calendar.
THE DEADLINE IS THIS THURSDAY 06/28/2018.

Attached is the ad used in last years calendar. A few notes on this...
**. This is by no means the model to follow.
Please be creative and do what makes more sense marketing wise.
1. Need to update the color scheme which corresponds to the new website at marvolinlegal.com
2. The "MARVOLIN LAW | SHAPING FAITH WITH RESULTS" should be put at the top and made larger
3. "KNOWN AND TRUSTED IN OUR COMMUNITY FOR OVER 21 YEARS" should be changed to "KNOWN AND TRUSTED IN OUR COMMUNITY FOR OVER 22 YEARS"
4. "Gordon R. Marvolin, Esq." should be made larger and better positioned.
5. Under the list of practices, it should be changed to have:
"Personal Injury, Legal Malpractice, Unlicensed Contractors, Medical Malpractice, Civil Litigation"
6. Contact information (i.e. contact number, website, and address) should be better positioned
7. Placement of endorsement logos should stand out more.
8. New picture of head attorney is attached.

Last but not least... Give it your best shot!

```html
<!DOCTYPE html>
<html lang="en">
<head>
<meta charset="utf-8">
<title>Marvolin Law – Calendar Ad</title>
<link href="https://fonts.googleapis.com/css2?family=Montserrat:wght@500&family=Open+Sans:wght@300;400;600;700&display=swap" rel="stylesheet">
<style>
  :root {
    --ink: #1a1a1a;
    --gold: #c7a671;
    --gold-light: #ddc49a;
    --slate: #5d5d5d;
    --white: #ffffff;
    --paper: #f4f4f4;
    --badge-red: #c8261e;
    --badge-maroon: #7a1c1c;
    --badge-bronze: #a38a54;
    --badge-blue: #1d6fb3;
    --badge-navy: #16517f;
  }
  html, body { margin: 0; padding: 0; overflow: hidden; }
  body { width: 1200px; height: 918px; background: var(--paper); }
  .ad {
    position: relative; width: 1200px; height: 918px; overflow: hidden;
    font-family: "Open Sans", Arial, sans-serif; color: var(--white);
  }
  .ad-shapes { position: absolute; inset: 0; }
  .brand { position: absolute; left: 33px; top: 58px; display: flex; align-items: flex-start; gap: 50px; }
  .brand-square { width: 112px; height: 112px; background: var(--gold); flex: none; }
  .brand-text { padding-top: 22px; }
  .brand-name {
    font-family: "Montserrat", Arial, sans-serif; font-weight: 500; font-size: 44px;
    letter-spacing: 4px; color: var(--gold); line-height: 1; margin: 0;
  }
  .brand-tagline { font-size: 18px; letter-spacing: 0.3px; margin: 18px 0 0; line-height: 1; }
  .headline {
    position: absolute; left: 33px; top: 252px; margin: 0;
    font-weight: 700; font-size: 29px; line-height: 40px; letter-spacing: -0.3px;
  }
  .attorney-name {
    position: absolute; left: 33px; top: 414px; margin: 0;
    font-weight: 600; font-size: 39px; line-height: 1; letter-spacing: -0.5px;
  }
  .practice-list { position: absolute; left: 33px; top: 512px; margin: 0; padding: 0; list-style: none; }
  .practice-item { display: flex; align-items: center; height: 31px; font-weight: 400; font-size: 25px; line-height: 1; }
  .practice-icon {
    width: 24px; height: 24px; margin-right: 13px; border: 2px solid var(--gold);
    border-radius: 50%; box-sizing: border-box; display: flex; align-items: center; justify-content: center; flex: none;
  }
  .offer { position: absolute; left: 33px; top: 676px; margin: 0; font-weight: 700; font-size: 24px; line-height: 34px; letter-spacing: -0.3px; }
  .contact { position: absolute; left: 33px; top: 724px; display: flex; align-items: center; color: var(--gold); font-weight: 700; font-size: 29px; line-height: 1; }
  .contact-item { display: flex; align-items: center; gap: 12px; margin-right: 22px; }
</style>
</head>
<body>
<div class="ad">
  <svg class="ad-shapes" width="1200" height="918" viewBox="0 0 1200 918">
    <defs>
      <linearGradient id="darkField" x1="0" y1="0" x2="1" y2="1">
        <stop offset="0" stop-color="#222"/><stop offset="1" stop-color="#141414"/>
      </linearGradient>
      <linearGradient id="officeTones" x1="0" y1="0" x2="1" y2="1">
        <stop offset="0" stop-color="#b79c86"/><stop offset="0.45" stop-color="#8a6b55"/>
        <stop offset="0.75" stop-color="#9a9ea3"/><stop offset="1" stop-color="#d9d9db"/>
      </linearGradient>
    </defs>
    <rect class="city-backdrop" width="1200" height="788" fill="url(#darkField)" role="img" aria-label="Faint dark city skyline backdrop"/>
    <rect class="badge-strip" y="788" width="1200" height="130" fill="var(--white)"/>
    <polygon class="divider-band" points="805,0 850,0 593,442 845,918 790,918 548,442" fill="var(--slate)"/>
    <polygon class="portrait" points="842,0 1200,0 1200,918 848,918 600,442" fill="url(#officeTones)" role="img" aria-label="Portrait of attorney Gordon R. Marvolin in a grey suit and blue tie, standing in a law office"/>
    <polygon class="name-band" points="0,387 563,387 513,442 563,497 0,497" fill="var(--gold)"/>
    <polygon class="name-chevron" points="563,387 585,387 536,442 585,497 563,497 513,442" fill="var(--gold-light)"/>
    <polygon class="offer-band" points="0,675 402,675 394,709 0,709" fill="var(--slate)"/>
    <g class="endorsements">
      <rect x="31" y="810" width="119" height="78" rx="4" fill="var(--badge-red)"/>
      <circle cx="228" cy="848" r="41" fill="var(--badge-maroon)"/>
      <rect x="292" y="806" width="96" height="76" rx="4" fill="var(--badge-bronze)"/>
      <circle cx="463" cy="843" r="40" fill="var(--badge-blue)"/>
      <rect x="536" y="808" width="174" height="66" rx="8" fill="var(--badge-navy)"/>
    </g>
  </svg>

  <header class="brand">
    <div class="brand-square"></div>
    <div class="brand-text">
      <h1 class="brand-name">MARVOLIN LAW</h1>
      <p class="brand-tagline">SHAPING FAITH WITH RESULTS</p>
    </div>
  </header>

  <p class="headline">KNOWN AND TRUSTED IN OUR<br>COMMUNITY FOR OVER 22 YEARS</p>

  <h2 class="attorney-name">Gordon R. Marvolin, Esq.</h2>

  <ul class="practice-list">
    <li class="practice-item"><span class="practice-icon"><svg width="12" height="10" viewBox="0 0 12 10"><path d="M1 5l3.5 3.5L11 1.5" fill="none" stroke="var(--gold)" stroke-width="2"/></svg></span>Personal Injury</li>
    <li class="practice-item"><span class="practice-icon"><svg width="12" height="10" viewBox="0 0 12 10"><path d="M1 5l3.5 3.5L11 1.5" fill="none" stroke="var(--gold)" stroke-width="2"/></svg></span>Legal Malpractice</li>
    <li class="practice-item"><span class="practice-icon"><svg width="12" height="10" viewBox="0 0 12 10"><path d="M1 5l3.5 3.5L11 1.5" fill="none" stroke="var(--gold)" stroke-width="2"/></svg></span>Unlicensed Contractors</li>
    <li class="practice-item"><span class="practice-icon"><svg width="12" height="10" viewBox="0 0 12 10"><path d="M1 5l3.5 3.5L11 1.5" fill="none" stroke="var(--gold)" stroke-width="2"/></svg></span>Medical Malpractice</li>
    <li class="practice-item"><span class="practice-icon"><svg width="12" height="10" viewBox="0 0 12 10"><path d="M1 5l3.5 3.5L11 1.5" fill="none" stroke="var(--gold)" stroke-width="2"/></svg></span>Civil Litigation</li>
  </ul>

  <p class="offer">FREE CONSULTATION TODAY!</p>

  <div class="contact">
    <span class="contact-item">
      <svg width="30" height="30" viewBox="0 0 34 34"><circle cx="17" cy="17" r="17" fill="var(--gold)"/><path d="M11 9c1-1 2-1 3 0l2 3c.5 1 0 2-1 2.5 1 2.5 3 4.5 5.5 5.5.5-1 1.5-1.5 2.5-1l3 2c1 1 1 2 0 3-2 2-5 2-9-1.5S7.5 15 9 11z" fill="var(--ink)"/></svg>
      310.555.0147
    </span>
    <span class="contact-item">
      <svg width="28" height="28" viewBox="0 0 32 32" fill="none" stroke="var(--gold)" stroke-width="2.4"><circle cx="16" cy="16" r="13"/><ellipse cx="16" cy="16" rx="6" ry="13"/><path d="M3 16h26M5 9h22M5 23h22"/></svg>
      www.marvolinlegal.com
    </span>
  </div>
</div>
</body>
</html>
```